Labels design for moisturizer cream and Serum

We need our label to be design for our two skincare products - moisturizer & Serum.
The products are premium so they need to look clean and prestigious. Have it look similar to our logo (Attached for now with watermarks)

The 2 product names are:
Velvet Dawn Facial Serum
Moonpetal Glow Moisturizer

```html
<!DOCTYPE html>
<html lang="en">
<head>
<meta charset="utf-8">
<title>Velmora skincare labels</title>
<link rel="stylesheet" href="https://fonts.googleapis.com/css2?family=Montserrat:wght@400;600&display=swap">
<style>
  :root {
    --paper: #f5f5f5;
    --brand-grey: #b3b3b3;
    --moist-brown: #4b1f18;
    --serum-amber: #6a2a15;
    --gold: #c8a66a;
    --gold-deep: #8f6a3a;
    --ink-light: #ffffff;
    --ink-soft: #eadbd2;
  }
  * { box-sizing: border-box; margin: 0; padding: 0; }
  html, body { width: 1200px; height: 907px; overflow: hidden; background: var(--paper); }
  body { font-family: "Montserrat", sans-serif; position: relative; }

  .brand-mark {
    position: absolute; left: 560px; top: 88px; width: 570px;
    display: flex; flex-direction: column; align-items: center;
    color: var(--brand-grey); font-weight: 400;
  }
  .brand-mark__name { font-size: 122px; line-height: 1; letter-spacing: -3px; white-space: nowrap; }
  .brand-mark__rule { width: 100%; height: 2px; background: var(--brand-grey); margin-top: 10px; }
  .brand-mark__place { font-size: 28px; letter-spacing: 72px; margin-right: -72px; line-height: 1; margin-top: 10px; }

  .label {
    position: absolute; display: flex; flex-direction: column; align-items: center;
    color: var(--ink-light); text-align: center;
  }
  .label--moisturizer { left: 146px; top: 420px; width: 210px; height: 430px; background: var(--moist-brown); border-radius: 4px; padding-top: 38px; }
  .label--serum { left: 442px; top: 518px; width: 240px; height: 330px; background: var(--serum-amber); border-radius: 4px; padding-top: 60px; }

  .label__brand { font-weight: 400; font-size: 34px; line-height: 1; white-space: nowrap; }
  .label__place {
    font-size: 9px; letter-spacing: 10px; margin-right: -10px; line-height: 1;
    margin-top: 3px; padding-top: 2px; border-top: 1px solid var(--ink-light); width: 150px;
  }
  .label__rule { width: 170px; height: 1px; background: var(--gold); }
  .label__rule--top { margin-top: 70px; }
  .label--serum .label__rule--top { margin-top: 38px; }
  .label__product { font-weight: 600; font-size: 14px; letter-spacing: 0.8px; line-height: 1.3; padding: 6px 0; }
  .label__claim { font-size: 13px; color: var(--ink-soft); margin-top: 8px; line-height: 1.2; }
  .label__pattern {
    width: 190px; height: 60px; margin-top: 52px;
    background: linear-gradient(90deg, var(--gold-deep), var(--gold), var(--gold-deep));
    opacity: 0.55; border-radius: 2px;
  }
  .label--serum .label__pattern { margin-top: 10px; width: 196px; height: 50px; }
  .label__volume { font-size: 12px; color: var(--ink-soft); margin-top: 22px; }
  .label--serum .label__volume { margin-top: 8px; }
</style>
</head>
<body>
  <div class="brand-mark">
    <div class="brand-mark__name">VELMORA</div>
    <div class="brand-mark__rule"></div>
    <div class="brand-mark__place">PARIS</div>
  </div>

  <section class="label label--moisturizer">
    <div class="label__brand">VELMORA</div>
    <div class="label__place">PARIS</div>
    <div class="label__rule label__rule--top"></div>
    <div class="label__product">MOONPETAL GLOW<br>MOISTURIZER</div>
    <div class="label__rule"></div>
    <div class="label__claim">Broad Spectrum SPF 30</div>
    <div class="label__pattern" role="img" aria-label="Gold lace ornament band"></div>
    <div class="label__volume">℮59 mL / 2 fl oz</div>
  </section>

  <section class="label label--serum">
    <div class="label__brand">VELMORA</div>
    <div class="label__place">PARIS</div>
    <div class="label__rule label__rule--top"></div>
    <div class="label__product">VELVET DAWN<br>FACIAL SERUM</div>
    <div class="label__rule"></div>
    <div class="label__claim">Roseship CO₂</div>
    <div class="label__pattern" role="img" aria-label="Gold lace ornament band"></div>
    <div class="label__volume">℮30 mL / 1 oz</div>
  </section>
</body>
</html>
```